PressLeaf Design Project

NOTICE TO DESIGNERS
****************NOTE: PLEASE DO NOT SUBMIT ANY MORE DESIGNS, THANK YOU!!!!****************
The name of our business is Harbor Pixel Guild and we are setting up a website to review new phones/tablets in the marketplace.
We require a 5 page design, the idea behind the project can be understood better if you visit this websites
1) tallowbrook.example
2) http://vrnqo.example/reviews/cellphones/
Pages required are;
1) Home page which lists all the current top devices
2) A single device page that shows the device with its current specs
3) Comparison page - where 2 or 3 devices are being compared in terms of specs
4) Archive page that shows all the current videos and text reviews
5) Single post page for the device being reviewed with all its pictures, written review, video with sidebar on the side showing other reviews available.
I am opened to a nice color scheme, including red, blue and orange. We do not have any logo at the moment. Thanks
This is a notice to all designers, I have found the designer I want to work with please do not submit any more designs for now. Thank you

```html
<!DOCTYPE html>
<html lang="en">
<head>
<meta charset="utf-8">
<title>Harbor Pixel Guild — Phones</title>
<link href="https://fonts.googleapis.com/css2?family=Open+Sans:wght@400;600;700;800&display=swap" rel="stylesheet">
<style>
:root{
  --orange:#f7a600;
  --orange-dark:#e08e00;
  --ink:#333;
  --muted:#888;
  --line:#e2e2e2;
  --page:#f2f2f2;
  --white:#fff;
  --footer:#2b2b2b;
  --footer-deep:#1f1f1f;
  --footer-text:#a9a9a9;
  --badge:#e2401c;
}
*{box-sizing:border-box;margin:0;padding:0}
html,body{width:729px;height:1200px;overflow:hidden}
body{font-family:"Open Sans",Arial,sans-serif;color:var(--ink);background:var(--page)}
.canvas{position:relative;width:729px;height:1200px;overflow:hidden;background:var(--page)}

/* header */
.site-header{position:absolute;left:0;top:0;width:729px;height:60px;background:var(--white)}
.brand{position:absolute;left:97px;top:12px;color:var(--orange);font-weight:800;font-size:17px;line-height:17px;letter-spacing:.3px}
.search{position:absolute;left:338px;top:20px;width:156px;height:14px;border:1px solid var(--line);display:flex}
.search span{flex:1;font-size:6px;color:var(--muted);padding:3px 4px}
.search i{width:14px;background:#ccc}
.account{position:absolute;left:570px;top:5px;width:62px;text-align:right}
.account .login{display:inline-block;background:var(--footer);color:var(--white);font-size:6px;padding:2px 6px;font-weight:700}
.account .links{font-size:6px;margin-top:6px;color:var(--ink);font-weight:600;white-space:nowrap}

/* nav */
.main-nav{position:absolute;left:97px;top:62px;width:535px;height:22px;background:var(--orange);display:flex;align-items:center;padding-left:8px;gap:17px}
.main-nav a{color:var(--white);font-size:8px;font-weight:700;text-decoration:none}

/* breadcrumb */
.crumbs{position:absolute;left:97px;top:91px;width:535px;height:14px;display:flex;gap:4px}
.crumbs span{font-size:5px;color:var(--muted);border:1px solid var(--line);background:var(--white);padding:2px 6px}

/* container */
.content{position:absolute;left:93px;top:110px;width:544px;height:848px;background:var(--white)}

/* sidebar */
.sidebar{position:absolute;left:97px;top:118px;width:128px}
.widget-title{font-size:10px;font-weight:800;color:var(--ink);border-bottom:1px solid var(--line);padding-bottom:3px;margin-bottom:5px}
.cat-list{list-style:none;font-size:6px;line-height:9.6px;color:#555}
.cat-list li.top{color:var(--orange);font-weight:700}
.cat-list li.sub{padding-left:8px}
.price-filter{position:absolute;left:97px;top:574px;width:128px}
.slider{height:4px;background:var(--line);position:relative;margin:6px 0 8px}
.slider b{position:absolute;left:0;top:0;height:4px;width:100%;background:var(--orange)}
.filter-row{display:flex;justify-content:space-between;font-size:6px;color:var(--muted)}
.btn{display:inline-block;background:#e6e6e6;color:#555;font-size:5px;font-weight:700;padding:2px 6px;border:1px solid #d6d6d6}
.promo{position:absolute;left:97px;top:650px;width:128px;height:130px;background:linear-gradient(#d9d9d9,#cfcfcf)}
.promo-cta{position:absolute;left:129px;top:790px;width:64px;height:14px;background:var(--orange);color:var(--white);font-size:6px;font-weight:700;text-align:center;line-height:14px}
.custom-html{position:absolute;left:97px;top:822px;width:128px}
.custom-html p{font-size:6px;line-height:9px;color:#666;margin-bottom:9px}

/* main column */
.hero{position:absolute;left:240px;top:118px;width:392px;height:138px;background:linear-gradient(135deg,#f4f4f4,#dcdcdc)}
.pager{position:absolute;left:240px;width:392px;height:14px;display:flex;align-items:center;justify-content:space-between;font-size:5.5px;color:var(--muted);border-top:1px solid var(--line);border-bottom:1px solid var(--line)}
.pager .pages{display:flex;gap:2px;align-items:center}
.pager .pages b{display:inline-block;width:9px;height:9px;border:1px solid var(--line);font-weight:400;text-align:center;line-height:8px}
.pager .pages b.on{background:var(--orange);color:var(--white);border-color:var(--orange)}
.pager-top{top:263px}
.pager-bottom{top:940px}

.products{position:absolute;left:240px;top:292px;width:392px;display:grid;grid-template-columns:repeat(4,92px);column-gap:8px;row-gap:0}
.product{height:160px;position:relative}
.product .thumb{width:74px;height:74px;background:var(--orange)}
.product .badge{position:absolute;left:0;top:0;width:20px;height:20px;background:var(--badge);clip-path:polygon(0 0,100% 0,0 100%)}
.product .badge span{position:absolute;left:-1px;top:4px;width:14px;text-align:center;color:var(--white);font-size:3.6px;font-weight:700;line-height:4px;transform:rotate(-45deg)}
.product h3{font-size:6px;font-weight:600;line-height:8px;margin-top:5px;width:72px;color:#444}
.product .price{font-size:6px;color:var(--orange-dark);font-weight:700;margin-top:3px}
.product .price s{color:var(--muted);font-weight:400;margin-left:3px}
.product .btn{margin-top:12px;margin-left:18px}

/* footer */
.site-footer{position:absolute;left:0;top:965px;width:729px;height:235px;background:var(--footer)}
.footer-strip{height:28px;border-bottom:1px solid #3a3a3a;display:flex;align-items:center;justify-content:space-between;padding:0 97px}
.socials{display:flex;gap:6px}
.socials i{width:10px;height:10px;border-radius:50%;background:#555}
.shipping-note{font-size:6px;color:var(--footer-text);font-weight:700;letter-spacing:.3px}
.footer-cols{display:flex;padding:14px 97px 0;gap:0}
.footer-col{width:107px}
.footer-col h4{font-size:7px;color:var(--white);font-weight:700;margin-bottom:6px}
.footer-col ul{list-style:none;font-size:5.5px;line-height:8.5px;color:var(--footer-text)}
.footer-bottom{position:absolute;left:0;top:203px;width:729px;height:32px;background:var(--footer-deep);display:flex;align-items:center;justify-content:space-between;padding:0 97px}
.footer-bottom small{font-size:5.5px;color:var(--footer-text)}
.cards{display:flex;gap:3px}
.cards i{width:16px;height:10px;background:#d8d8d8;border-radius:1px}
</style>
</head>
<body>
<div class="canvas">

  <header class="site-header">
    <div class="brand">HARBOR PIXEL<br>GUILD</div>
    <div class="search"><span>Search here...</span><i></i></div>
    <div class="account">
      <span class="login">LOGIN</span>
      <div class="links">Register &nbsp;|&nbsp; Sign In</div>
    </div>
  </header>

  <nav class="main-nav">
    <a>Home</a><a>Top Phones</a><a>Gadgets</a><a>Latest Phones</a><a>Appliances</a><a>Custom Block</a><a>Custom Block 2</a>
  </nav>

  <div class="crumbs"><span>Home</span><span>Phones</span><span>Accessories</span></div>

  <div class="content"></div>

  <aside class="sidebar">
    <h2 class="widget-title">PHONES</h2>
    <ul class="cat-list">
      <li class="top">» Phones</li>
      <li class="sub">Flagship</li><li class="sub">Budget</li><li class="sub">Foldables</li><li class="sub">Rugged</li><li class="sub">Compact</li>
      <li class="top">» Deals</li>
      <li class="sub">Latest Deals</li><li class="sub">Bags and Cases</li><li class="sub">Screens</li><li class="sub">New</li><li class="sub">Top and Best</li><li class="sub">Chargers</li><li class="sub">Cables and Docks</li>
      <li class="top">» Business Phones</li>
      <li class="sub">Cases</li><li class="sub">Chargers and Bags</li><li class="sub">Docks</li><li class="sub">Screens</li><li class="sub">Batteries</li><li class="sub">Bundles and Sets</li><li class="sub">Docks and Speakers</li><li class="sub">Mobile Phones</li><li class="sub">Latest this year</li>
      <li class="top">» Accessories</li>
      <li class="sub">Car Holders</li><li class="sub">Home Docks</li><li class="sub">Memory Cards</li><li class="sub">Pens</li><li class="sub">Spare Parts</li><li class="sub">Lights and Lamps</li><li class="sub">Headsets</li><li class="sub">Speakers</li><li class="sub">Sim Tools</li><li class="sub">Protectors</li><li class="sub">Fragrances</li>
      <li class="top">» Mobile Phones</li>
      <li class="top">» Smart Phones</li>
      <li class="top">» Smart Phone Prices</li>
      <li class="top">» Mobile Phones</li>
      <li class="top">» Top Lists of Phones</li>
    </ul>
  </aside>

  <section class="price-filter">
    <h2 class="widget-title">FILTER BY PRICE</h2>
    <div class="slider"><b></b></div>
    <div class="filter-row"><span class="btn">FILTER</span><span>Price: $0 — $500</span></div>
  </section>

  <div class="promo" role="img" aria-label="Sponsor banner for the PressLeaf platform"></div>
  <div class="promo-cta">LEARN MORE</div>

  <section class="custom-html">
    <h2 class="widget-title">CUSTOM HTML</h2>
    <p>This is HTML block. You can use it to add any text or images. Content can be edited from the theme options panel with ease.</p>
    <p>This text block is a simple sample of custom content that can be placed here to suit your needs.</p>
    <p>Thanks</p>
  </section>

  <div class="hero" role="img" aria-label="Featured phone banner photo"></div>

  <div class="pager pager-top">
    <span>THERE ARE TWO ITEMS ON 17 PAGES</span>
    <span class="pages">PAGE <b>1</b><b>2</b><b class="on">3</b><b>4</b><b>›</b></span>
  </div>

  <main class="products">
    <article class="product"><div class="thumb" role="img" aria-label="Product photo"></div><span class="badge"><span>NEW</span></span><h3>Nice Leather Fashion Demo Shoes</h3><div class="price">$159.00<s>$199.00</s></div><span class="btn">ADD TO CART</span></article>
    <article class="product"><div class="thumb" role="img" aria-label="Product photo"></div><h3>Nice Leather Fashion Demo Shoes</h3><div class="price">$159.00<s>$199.00</s></div><span class="btn">ADD TO CART</span></article>
    <article class="product"><div class="thumb" role="img" aria-label="Product photo"></div><h3>Nice Leather Fashion Demo Shoes</h3><div class="price">$159.00<s>$199.00</s></div><span class="btn">ADD TO CART</span></article>
    <article class="product"><div class="thumb" role="img" aria-label="Product photo"></div><h3>Nice Leather Fashion Demo Shoes</h3><div class="price">$159.00<s>$199.00</s></div><span class="btn">ADD TO CART</span></article>

    <article class="product"><div class="thumb" role="img" aria-label="Product photo"></div><span class="badge"><span>NEW</span></span><h3>Nice Leather Fashion Demo Shoes</h3><div class="price">$159.00<s>$199.00</s></div><span class="btn">ADD TO CART</span></article>
    <article class="product"><div class="thumb" role="img" aria-label="Product photo"></div><h3>Nice Leather Fashion Demo Shoes</h3><div class="price">$159.00<s>$199.00</s></div><span class="btn">ADD TO CART</span></article>
    <article class="product"><div class="thumb" role="img" aria-label="Product photo"></div><h3>Nice Leather Fashion Demo Shoes</h3><div class="price">$159.00<s>$199.00</s></div><span class="btn">ADD TO CART</span></article>
    <article class="product"><div class="thumb" role="img" aria-label="Product photo"></div><h3>Nice Leather Fashion Demo Shoes</h3><div class="price">$159.00<s>$199.00</s></div><span class="btn">ADD TO CART</span></article>

    <article class="product"><div class="thumb" role="img" aria-label="Product photo"></div><span class="badge"><span>NEW</span></span><h3>Nice Leather Fashion Demo Shoes</h3><div class="price">$159.00<s>$199.00</s></div><span class="btn">ADD TO CART</span></article>
    <article class="product"><div class="thumb" role="img" aria-label="Product photo"></div><h3>Nice Leather Fashion Demo Shoes</h3><div class="price">$159.00<s>$199.00</s></div><span class="btn">ADD TO CART</span></article>
    <article class="product"><div class="thumb" role="img" aria-label="Product photo"></div><h3>Nice Leather Fashion Demo Shoes</h3><div class="price">$159.00<s>$199.00</s></div><span class="btn">ADD TO CART</span></article>
    <article class="product"><div class="thumb" role="img" aria-label="Product photo"></div><h3>Nice Leather Fashion Demo Shoes</h3><div class="price">$159.00<s>$199.00</s></div><span class="btn">ADD TO CART</span></article>

    <article class="product"><div class="thumb" role="img" aria-label="Product photo"></div><span class="badge"><span>NEW</span></span><h3>Nice Leather Fashion Demo Shoes</h3><div class="price">$159.00<s>$199.00</s></div><span class="btn">ADD TO CART</span></article>
    <article class="product"><div class="thumb" role="img" aria-label="Product photo"></div><h3>Nice Leather Fashion Demo Shoes</h3><div class="price">$159.00<s>$199.00</s></div><span class="btn">ADD TO CART</span></article>
    <article class="product"><div class="thumb" role="img" aria-label="Product photo"></div><h3>Nice Leather Fashion Demo Shoes</h3><div class="price">$159.00<s>$199.00</s></div><span class="btn">ADD TO CART</span></article>
    <article class="product"><div class="thumb" role="img" aria-label="Product photo"></div><h3>Nice Leather Fashion Demo Shoes</h3><div class="price">$159.00<s>$199.00</s></div><span class="btn">ADD TO CART</span></article>
  </main>

  <div class="pager pager-bottom">
    <span>THERE ARE TWO ITEMS ON 17 PAGES</span>
    <span class="pages">PAGE <b>1</b><b>2</b><b class="on">3</b><b>4</b><b>›</b></span>
  </div>

  <footer class="site-footer">
    <div class="footer-strip">
      <div class="socials"><i></i><i></i><i></i><i></i></div>
      <span class="shipping-note">FREE SHIPPING ON ALL ORDERS FROM US</span>
    </div>
    <div class="footer-cols">
      <div class="footer-col"><h4>YOUR ORDERS</h4><ul><li>Order Status</li><li>Track Orders</li><li>Returns</li><li>Gift Cards</li><li>Order History</li><li>Wish List</li><li>Help Center</li></ul></div>
      <div class="footer-col"><h4>SHIPPING INFO</h4><ul><li>Delivery Times</li><li>Shipping Rates</li><li>International</li><li>Express Options</li><li>Store Pickup</li><li>FAQ</li></ul></div>
      <div class="footer-col"><h4>MY ACCOUNT</h4><ul><li>Sign In</li><li>Register</li><li>Profile</li><li>Addresses</li><li>Newsletter</li><li>Settings</li></ul></div>
      <div class="footer-col"><h4>SITE LINKS</h4><ul><li>Site Map</li><li>Search Terms</li><li>Advanced Search</li><li>Contact Us</li><li>About Us</li><li>Reviews</li></ul></div>
      <div class="footer-col"><h4>CHIRPLINE</h4><ul><li>New phone review posted today,</li><li>read the full specs now.</li><li>3 hours ago</li><li>Tablet comparison is live,</li><li>see which one wins.</li><li>1 day ago</li></ul></div>
    </div>
    <div class="footer-bottom">
      <small>© 2013 Harbor Pixel Guild. All Rights Reserved.</small>
      <div class="cards"><i></i><i></i><i></i><i></i><i></i></div>
    </div>
  </footer>

</div>
</body>
</html>
```